Bluefern Project Services - Flyer

Project Breif:
I need a single page A4 Capability Statement, which will be used to market our services to prospective clients, both in print and via email PDF.
It needs to look professional and should incorporate the elements I have uploaded into files, these include:
Capability Statement Text
Bluefern Services Company Logo
Additional Logo’s (Tools We Use)
Frame Barn Pics can be cut into the page
I have included examples of capability statements as a guide to what i am looking for.
Regards
Derek
Engineering Consulting

```html
<!DOCTYPE html>
<html lang="en">
<head>
<meta charset="utf-8">
<title>Bluefern Project Services – Capability Statement</title>
<link rel="stylesheet" href="https://fonts.googleapis.com/css2?family=Arimo:wght@400;700&family=Montserrat:wght@400;500;700;800&family=Questrial&display=swap">
<style>
  :root {
    --backdrop: #a9aaad;
    --paper: #ffffff;
    --panel: #f6f6f6;
    --band: rgba(80, 82, 86, 0.88);
    --blue: #1479c6;
    --heading-blue: #1477c2;
    --ink: #2b2b2b;
    --body: #555a5f;
    --tool-ink: #4a4d52;
    --logo-ink: #2d2f33;
    --logo-grey: #9ea3a8;
  }
  * { box-sizing: border-box; margin: 0; padding: 0; }
  html, body { width: 979px; height: 1200px; overflow: hidden; }
  body { background: var(--backdrop); font-family: "Arimo", Arial, sans-serif; position: relative; }

  .flyer {
    position: absolute; left: 71px; top: 8px;
    width: 836px; height: 1183px;
    background: var(--paper);
    overflow: hidden;
  }

  .hero {
    position: absolute; left: 0; top: 0; width: 836px; height: 488px;
    background:
      radial-gradient(ellipse at 70% 55%, #f3ece8 0%, rgba(243,236,232,0) 45%),
      radial-gradient(ellipse at 20% 40%, #e7ddd8 0%, rgba(231,221,216,0) 40%),
      linear-gradient(120deg, #eef2f6 0%, #dfe6ee 35%, #f4f1ef 60%, #c9d6e4 100%);
  }

  .brand {
    position: absolute; left: 40px; top: 38px; width: 172px;
    display: flex; flex-direction: column; align-items: center;
  }
  .brand-dot { width: 54px; height: 54px; border-radius: 50%; background: var(--logo-grey); margin-bottom: 16px; }
  .brand-name {
    font-family: "Montserrat", sans-serif; font-weight: 700; color: var(--logo-ink);
    font-size: 14.5px; letter-spacing: 0.5px; white-space: nowrap; text-align: center; line-height: 1.15;
  }
  .brand-name .sub { display: block; font-size: 10px; letter-spacing: 6px; }

  .title-band {
    position: absolute; left: 0; top: 427px; width: 836px; height: 61px;
    background: var(--band);
    display: flex; align-items: center; justify-content: center;
  }
  .title-band h1 {
    font-family: "Questrial", sans-serif; font-weight: 400; color: #fff;
    font-size: 36px; letter-spacing: 0.5px; padding-right: 18px;
  }

  .about {
    position: absolute; left: 0; top: 503px; width: 407px; height: 545px;
    background: var(--panel);
    padding: 38px 54px 0 66px;
  }
  .about .lead { color: var(--blue); font-size: 19.5px; line-height: 22px; margin-bottom: 22px; width: 282px; }
  .about p { color: var(--body); font-size: 18px; line-height: 20.4px; margin-bottom: 20.5px; }

  .services { position: absolute; left: 434px; top: 510px; width: 380px; }
  .services h2 {
    font-family: "Questrial", sans-serif; font-weight: 400; font-size: 29px; color: var(--ink);
    border-left: 5px solid var(--blue); padding-left: 10px; line-height: 28px; letter-spacing: 1.5px;
  }
  .services h3 {
    font-family: "Montserrat", sans-serif; font-weight: 800; font-size: 18.5px; color: var(--heading-blue);
    margin: 14px 0 8px 15px; letter-spacing: -0.2px;
  }
  .services h3.spaced { margin-top: 22px; }
  .services ul { list-style: none; margin-left: 42px; }
  .services li { font-size: 15.5px; color: var(--ink); line-height: 20.8px; position: relative; }
  .services li::before {
    content: ""; position: absolute; left: -12px; top: 8px; width: 4px; height: 4px;
    border-radius: 50%; background: var(--blue);
  }

  .tools {
    position: absolute; left: 48px; top: 1070px; width: 742px; height: 40px;
    display: flex; align-items: center; justify-content: space-between;
    font-family: "Montserrat", sans-serif; font-weight: 700; font-size: 14px;
  }
  .tool { color: var(--tool-ink); white-space: nowrap; }

  .footer {
    position: absolute; left: 0; top: 1122px; width: 836px; height: 61px;
    background: var(--blue); color: #fff;
    font-family: "Montserrat", sans-serif;
    display: flex; align-items: center;
  }
  .contact-person { padding-left: 55px; width: 212px; flex-shrink: 0; }
  .contact-person .name { font-size: 15px; font-weight: 500; line-height: 18px; white-space: nowrap; }
  .contact-person .role { font-size: 10.5px; white-space: nowrap; }
  .contact-item {
    display: flex; align-items: center; gap: 7px; font-size: 13.5px; padding: 0 15px; height: 36px;
    white-space: nowrap; flex-shrink: 0;
  }
  .contact-item + .contact-item { border-left: 1px solid rgba(255,255,255,0.75); }
  .contact-item svg { width: 17px; height: 17px; fill: none; stroke: #fff; stroke-width: 1.4; flex-shrink: 0; }
</style>
</head>
<body>
<main class="flyer">
  <section class="hero" role="img" aria-label="Photo of colleagues at a desk reviewing printed project charts and documents">
    <div class="brand">
      <span class="brand-dot"></span>
      <span class="brand-name">BLUEFERN PROJECT<span class="sub">SERVICES</span></span>
    </div>
  </section>

  <div class="title-band"><h1>CAPABILITY STATEMENT</h1></div>

  <section class="about">
    <p class="lead">Bluefern Project Services Ltd.is a leading project control consultancy based in Co Cork Ireland</p>
    <p>For over 20 years we have been helping our clients to deliver complex projects and programs throughout mainland Europe.</p>
    <p>We are passionate about empower organisations to achieve their objectives, on time and on budget.</p>
    <p>We are continually innovating, evolving and learning, utilize the latest industry tools and techniques to deliver real value to our clients.</p>
    <p>Our goal is to make successful project delivery more achievable and repeatable.</p>
  </section>

  <section class="services">
    <h2>CORE SERVICES:</h2>
    <h3>PLANNING AND SCHEDULING</h3>
    <ul>
      <li>Tender Planning</li>
      <li>Interactive Planning / Pull Planning</li>
      <li>EPCMV Planning &amp; Scheduling</li>
      <li>Schedule Earned Value Management</li>
      <li>Independent Schedule Quality Assessment</li>
      <li>Schedule Risk Analysis (Monte Carlo)</li>
      <li>Training</li>
    </ul>
    <h3 class="spaced">MANAGEMENT OF RISK</h3>
    <ul>
      <li>Risk Management Policies &amp; Procedures</li>
      <li>Risk Management Strategy</li>
      <li>Risk Registers</li>
      <li>Risk Improvement Planning</li>
      <li>Risk Response and Communication</li>
      <li>Risk Management Training</li>
    </ul>
    <h3 class="spaced">COST CONTROL:</h3>
    <ul>
      <li>Estimating &amp; Forecasting</li>
      <li>Earned Value Analysis</li>
      <li>Progress Reporting</li>
      <li>Cost Risk Analysis</li>
    </ul>
  </section>

  <section class="tools" aria-label="Tools we use">
    <span class="tool">Cornerstone</span>
    <span class="tool">PlanDesk</span>
    <span class="tool">Arbor Scheduler</span>
    <span class="tool">Waypoint Pro</span>
    <span class="tool">Ledgerly</span>
    <span class="tool">Vantage</span>
    <span class="tool">RiskFrame</span>
  </section>

  <footer class="footer">
    <div class="contact-person">
      <div class="name">Derek Hollins</div>
      <div class="role">Managing Director</div>
    </div>
    <div class="contact-item">
      <svg viewBox="0 0 24 24"><path d="M5 3h4l2 5-3 2a12 12 0 0 0 6 6l2-3 5 2v4a2 2 0 0 1-2 2A17 17 0 0 1 3 5a2 2 0 0 1 2-2z"/></svg>
      +353 (0)870 415 226
    </div>
    <div class="contact-item">
      <svg viewBox="0 0 24 24"><rect x="3" y="5" width="18" height="14"/><path d="M3 5l9 8 9-8"/></svg>
      info@bluefernservices.ie
    </div>
    <div class="contact-item">
      <svg viewBox="0 0 24 24"><circle cx="12" cy="12" r="9"/><ellipse cx="12" cy="12" rx="4" ry="9"/><path d="M3 12h18M5 7h14M5 17h14"/></svg>
      www.bluefernservices.ie
    </div>
  </footer>
</main>
</body>
</html>
```